TalkWell needs a Letterhead

We need a letterhead for our company "TalkWell Consultants". Logo is attached. The company color is Turquoise. Icons for website, scan logo for website, icons for address, e-mail and phone appreciated rather than just words.

```html
<!DOCTYPE html>
<html lang="en">
<head>
<meta charset="utf-8">
<title>TalkWell Consultants Letterhead</title>
<link href="https://fonts.googleapis.com/css2?family=Open+Sans:wght@400;600&display=swap" rel="stylesheet">
<style>
  :root {
    --backdrop: #525252;
    --paper: #ffffff;
    --brand-blue: #1276bf;
    --brand-green: #8dc63f;
    --faint-blue: #e6f0f8;
    --ink: #333333;
    --rule: #9a9a9a;
  }
  * { box-sizing: border-box; margin: 0; padding: 0; }
  html, body {
    width: 1200px; height: 1000px; overflow: hidden;
    background: var(--backdrop);
    font-family: "Open Sans", Arial, sans-serif;
  }
  .letterhead {
    position: absolute; left: 267px; top: 30px;
    width: 665px; height: 940px;
    background: var(--paper);
    overflow: hidden;
  }
  .brand {
    position: absolute; right: 48px; top: 52px;
    display: flex; align-items: center; gap: 10px;
    color: var(--brand-blue);
    font-weight: 600; font-size: 26px; letter-spacing: -0.2px;
  }
  .brand-mark {
    width: 16px; height: 16px; border-radius: 50%;
    background: var(--brand-blue);
  }
  .brand-faint {
    position: absolute; left: 0; right: 0; top: 400px;
    text-align: center;
    color: var(--faint-blue);
    font-weight: 600; font-size: 120px; letter-spacing: -2px;
  }
  .contact {
    position: absolute; left: 50px; bottom: 46px;
    display: flex; gap: 12px;
    font-size: 9px; color: var(--ink); line-height: 12px;
  }
  .contact-group { display: flex; flex-direction: column; gap: 1px; }
  .contact-divider { width: 1px; border-left: 1px solid var(--rule); border-right: 1px solid var(--rule); width: 4px; }
  .contact-item { display: flex; align-items: center; gap: 4px; }
  .contact-icon { width: 10px; height: 10px; flex: none; }
  .footer-bands {
    position: absolute; left: 0; bottom: 0; width: 665px; height: 20px;
  }
</style>
</head>
<body>
  <main class="letterhead">
    <header class="brand">
      <span class="brand-mark"></span>
      <span class="brand-name">TalkWell Consultants</span>
    </header>

    <div class="brand-faint" aria-hidden="true">TalkWell</div>

    <footer class="contact">
      <div class="contact-group">
        <div class="contact-item">
          <svg class="contact-icon" viewBox="0 0 10 10"><rect width="10" height="10" fill="#1276bf"/><path d="M3 2.2 L4.2 3.6 L3.6 4.3 Q4.6 6 6 6.6 L6.6 6 L8 7.2 L7.2 8.2 Q3.4 7.4 2.2 3 Z" fill="#fff"/></svg>
          <span>03 9555 0142</span>
        </div>
        <div class="contact-item">
          <svg class="contact-icon" viewBox="0 0 10 10"><rect width="10" height="10" fill="#1276bf"/><rect x="2" y="4" width="6" height="3.5" fill="#fff"/><rect x="3" y="2" width="4" height="2" fill="#fff"/></svg>
          <span>03 9555 0143</span>
        </div>
        <div class="contact-item">
          <svg class="contact-icon" viewBox="0 0 10 10"><rect width="10" height="10" fill="#1276bf"/><rect x="2" y="3" width="6" height="4.5" fill="#fff"/><path d="M2 3 L5 5.6 L8 3" stroke="#1276bf" stroke-width="0.8" fill="none"/></svg>
          <span>info@talkwell.com.au</span>
        </div>
      </div>
      <div class="contact-divider"></div>
      <div class="contact-group">
        <div class="contact-item">
          <svg class="contact-icon" viewBox="0 0 10 10"><rect width="10" height="10" fill="#1276bf"/><circle cx="5" cy="5" r="3" fill="none" stroke="#fff" stroke-width="0.8"/><path d="M2 5 H8 M5 2 Q3.4 5 5 8 Q6.6 5 5 2" stroke="#fff" stroke-width="0.6" fill="none"/></svg>
          <span>www.talkwell.com.au</span>
        </div>
        <div class="contact-item">
          <svg class="contact-icon" viewBox="0 0 10 10"><rect width="10" height="10" fill="#1276bf"/><path d="M5 8.5 L2.8 5 A2.5 2.5 0 1 1 7.2 5 Z" fill="#fff"/><circle cx="5" cy="4" r="0.9" fill="#1276bf"/></svg>
          <span>12 Harbour Street, Westvale VIC 3000</span>
        </div>
      </div>
    </footer>

    <svg class="footer-bands" viewBox="0 0 665 20" aria-hidden="true">
      <path d="M0 5 H410 Q430 5 448 20 H0 Z" fill="var(--brand-blue)"/>
      <path d="M432 5 H665 V20 H460 Q450 10 432 5 Z" fill="var(--brand-green)"/>
    </svg>
  </main>
</body>
</html>
```